Poster for a Bicycle show/Expo

We need a poster for a Bicycle show/Expo and sustainable transport. Exhibitors will sell bikes, cycling clothing, accessories, etc. ...
This show is annual and the Poster is for the 2016 edition.

Your concept must be compatible in a landscape format. (We will ourselves adaptations of different formats.)
Width: 210 mm
Height: 297 mm
It's necessary for us to have the source file (vector) for make, later, the different format (flyers, website, ...)

Content of the Poster:
- 1 big picture (one of the two attached)
- Big title (typo-title worked): « Foire du Rouet » (« Salon » or « Salon du » can be small and « Vélo » big.)
- Subtitle: « et de la mobilité durable »
- Date: « 18, 19 et 20 mars 2016 » or « 18-20 mars 2016 »
- Place: « Halle RTP - Gare de Plantaz »
- Text line 1: « www.foire-du-rouet.ch »
- Text line 2: « Entrée gratuite »
- Text line 3: « Ve 18 mars de 17h à 20h - Sa 19 mars de 10h à 18h - Di 20 mars de 10h à 17h »
- Please, leave a zone in the poster for sponsors logos
(The predominant information (most visible) are: « Vélo » and « 18, 19 et 20 mars 2016 » or « 18-20 mars 2016 »)

Target Market(s)

Bicycle fan

Industry/Entity Type

Sporting Good

Font styles to use
Serif
Sans Serif

Colors
add136
ffffff
ec1f27

Requirements
Must have
• The style must be modern, dynamic, bright colors.

```html
<!DOCTYPE html>
<html lang="fr">
<head>
<meta charset="utf-8">
<title>Foire du Rouet 2016</title>
<link rel="stylesheet" href="https://fonts.googleapis.com/css2?family=Comfortaa:wght@400;700&family=Open+Sans:wght@400;600;700&display=swap">
<style>
  :root {
    --lime: #add136;
    --white: #ffffff;
    --red: #ec1f27;
    --sky-top: #1f6fc4;
    --sky-mid: #4f9ee0;
    --sky-low: #a9d4f2;
    --grass: #8cc63f;
    --grass-dark: #5f9a2a;
    --panel: rgba(255,255,255,0.88);
    --ink: #222;
    --blue: #1b5fa8;
    --orange: #f28c1c;
  }
  * { margin: 0; padding: 0; box-sizing: border-box; }
  html, body { width: 849px; height: 1200px; overflow: hidden; }
  body { font-family: "Open Sans", Arial, sans-serif; }
  .poster {
    position: relative; width: 849px; height: 1200px; overflow: hidden;
  }
  .backdrop {
    position: absolute; inset: 0;
    background:
      linear-gradient(180deg, transparent 0 76%, var(--grass) 84%, var(--grass-dark) 100%),
      linear-gradient(180deg, var(--sky-top) 0%, var(--sky-mid) 45%, var(--sky-low) 78%);
  }
  .rider {
    position: absolute; left: 0; top: 560px; width: 330px; height: 640px;
    background: radial-gradient(ellipse at 45% 45%, rgba(40,40,50,0.35), transparent 70%);
  }
  .headline { position: absolute; left: 0; right: 0; top: 0; text-align: center; color: var(--white); }
  .entry { position: absolute; top: 28px; width: 100%; font-size: 27px; font-weight: 400; }
  .kicker {
    position: absolute; top: 100px; width: 100%;
    font-family: "Comfortaa", "Open Sans", sans-serif; font-weight: 700;
    font-size: 44px; letter-spacing: 4px;
  }
  .kicker small { font-size: 40px; letter-spacing: 1px; }
  .title {
    position: absolute; top: 138px; width: 100%;
    font-family: "Comfortaa", "Open Sans", sans-serif; font-weight: 700;
    font-size: 132px; line-height: 1; letter-spacing: 2px; color: var(--lime);
  }
  .subtitle { position: absolute; top: 282px; width: 100%; font-size: 35px; font-weight: 400; }
  .date { position: absolute; top: 340px; width: 100%; font-size: 62px; font-weight: 700; color: var(--lime); }
  .venue { position: absolute; top: 418px; width: 100%; font-size: 30px; font-weight: 600; }
  .hours {
    position: absolute; top: 468px; left: 120px; right: 120px;
    display: flex; justify-content: space-between; font-size: 17px; line-height: 1.3; text-align: left;
  }
  .web { position: absolute; top: 545px; width: 100%; font-size: 27px; font-weight: 600; }
  .sponsors {
    position: absolute; left: 297px; top: 693px; width: 512px; height: 520px;
    background: var(--panel);
    display: grid; grid-template-columns: repeat(3, 1fr); grid-template-rows: repeat(7, 1fr);
    padding: 22px 16px 40px; gap: 6px 14px; align-items: center;
  }
  .sponsor {
    display: flex; align-items: center; justify-content: center; gap: 6px;
    font-weight: 700; font-size: 21px; letter-spacing: 0.5px;
  }
  .sponsor .dot { width: 14px; height: 14px; border-radius: 50%; background: currentColor; }
  .sponsor .sq { width: 14px; height: 14px; background: currentColor; }
  .c-green { color: #2e8b3a; } .c-blue { color: var(--blue); } .c-red { color: var(--red); }
  .c-ink { color: var(--ink); } .c-orange { color: var(--orange); } .c-grey { color: #777; }
</style>
</head>
<body>
<main class="poster">
  <div class="backdrop" role="img" aria-label="Photographie : cycliste en VTT sur une prairie verte sous un ciel bleu"></div>
  <div class="rider" role="img" aria-label="Emplacement de la cycliste sur son vélo"></div>

  <header class="headline">
    <p class="entry">Entrée gratuite</p>
    <p class="kicker">FOIRE <small>du</small></p>
    <h1 class="title">ROUET</h1>
    <p class="subtitle">et de la mobilité durable</p>
    <p class="date">18 – 20 mars 2016</p>
    <p class="venue">Halle RTP - Gare de Plantaz</p>
    <div class="hours">
      <p>Ve 18 mars<br>de 17h à 20h</p>
      <p>Sa 19 mars<br>de 10h à 18h</p>
      <p>Di 20 mars<br>de 10h à 17h</p>
    </div>
    <p class="web">www.foire-du-rouet.ch</p>
  </header>

  <section class="sponsors" aria-label="Partenaires">
    <span class="sponsor c-green">Gripwell</span>
    <span class="sponsor c-ink">Nodo</span>
    <span class="sponsor c-red">Fortena</span>
    <span class="sponsor c-red"><i class="dot"></i>Sella</span>
    <span class="sponsor c-ink">Kestra</span>
    <span class="sponsor c-orange">Tyrio</span>
    <span class="sponsor c-red">Bovella</span>
    <span class="sponsor c-grey">Lastrail</span>
    <span class="sponsor c-red">Kerno</span>
    <span class="sponsor c-orange"><i class="dot"></i>Zenca</span>
    <span class="sponsor c-ink">Lumo</span>
    <span class="sponsor c-blue">Novatrek</span>
    <span class="sponsor"></span>
    <span class="sponsor c-ink"><i class="sq"></i>Pedalon</span>
    <span class="sponsor c-red">Axio</span>
    <span class="sponsor c-red">Ridgeway</span>
    <span class="sponsor c-red">Drivo</span>
    <span class="sponsor c-blue">Swiftline</span>
    <span class="sponsor c-blue">Kaizo</span>
    <span class="sponsor c-blue">Montebello</span>
    <span class="sponsor c-orange">Orvex</span>
  </section>
</main>
</body>
</html>
```